Flyer for American Indian Elders on Dementia Warning Signs

We need a flyer designed for older adults who are American Indian or Alaska Native (in the U.S.).

Ideally, the flyer should complement the colors of our logos. The project logo and our organization logo are attached to the brief.

When people see the flyer we want them to feel that it represents their culture, is warm, and professional but relatable to older adults and people who have limited incomes.

I have attached an earlier draft of the document we designed ourselves BUT we want different and better.

It is for older adults who have trouble reading so:
1. you must use a font that is 11.5 points or larger
2. Do not put text over complex pictures or use shading with words
3. You can use a serif font for the heading, but should use san serif for the body text
4. There should be good contrast between the font color and background

Please do not use any images that include a head dress or pictures of American Indian people or things that are very traditional or "token" imagery.

We need to save a small space under the call out box/ somewhere on the flyer for other people to add their logo once they download.

Let us know if you have questions or need additional information.

Target Market(s)

Older American Indian people

Font styles to use
Serif
Sans Serif

Requirements
Must have
• Easy to read for older adults
Should not have
• indian headdress

```html
<!DOCTYPE html>
<html lang="en">
<head>
<meta charset="utf-8">
<title>10 Signs of Thinking or Memory Changes That Might Be Dementia</title>
<link rel="stylesheet" href="https://fonts.googleapis.com/css2?family=Montserrat:wght@300;400;500;700;800&display=swap">
<style>
  :root {
    --teal: #2b7f87;
    --teal-dark: #26747b;
    --band: #2e8188;
    --paper: #efefef;
    --paper-shade: #e6e6e6;
    --white: #ffffff;
    --rose: #a3655f;
    --sea: #5f9fa5;
    --red: #a8433c;
  }
  * { box-sizing: border-box; margin: 0; padding: 0; }
  html, body {
    width: 848px; height: 1200px; overflow: hidden;
    background: var(--paper);
    font-family: "Montserrat", Arial, sans-serif;
  }
  .flyer { position: relative; width: 848px; height: 1200px; background: var(--paper); overflow: hidden; }
  .backdrop { position: absolute; inset: 0; }

  .title {
    position: absolute; left: 46px; top: 34px;
    color: var(--teal); font-size: 39.5px; line-height: 46px;
    font-weight: 300; letter-spacing: 0.2px; white-space: nowrap;
  }
  .title strong { font-weight: 800; }

  .intro-band {
    position: absolute; left: 0; top: 133px; width: 848px; height: 163px;
    background: var(--band); color: var(--white);
    padding: 9px 46px 0 46px; font-size: 17px; line-height: 20px; font-weight: 400;
  }
  .intro-band p + p { margin-top: 20px; }

  .signs { list-style: none; }
  .sign {
    position: absolute; left: 49px; width: 550px;
    font-size: 14px; line-height: 17.5px; color: var(--teal-dark);
    font-weight: 400; letter-spacing: 0.2px;
  }
  .sign-head { padding-left: 23px; text-indent: -23px; }
  .sign-head b { font-weight: 700; font-size: 15.5px; letter-spacing: 0.6px; }
  .sign-note { padding-left: 23px; }
  .sign-points { list-style: none; padding-left: 20px; margin-top: 2px; }
  .sign-points li { padding-left: 9px; text-indent: -9px; }
  .sign-points li::before { content: "\2022"; font-size: 10px; margin-right: 4px; position: relative; top: -1px; }
  .sign-ten .sign-head { padding-left: 28px; text-indent: -28px; }
  .sign-ten .sign-note { padding-left: 28px; }

  .main-points {
    position: absolute; left: 598px; top: 311px; width: 250px; height: 581px;
    border-radius: 36px 0 0 36px;
    background: linear-gradient(180deg, var(--rose) 0%, #8c7d7e 50%, var(--sea) 100%);
    color: var(--white); padding: 26px 14px 0 31px;
    font-size: 17.5px; line-height: 22px; font-weight: 400;
  }
  .main-points h2 { font-size: 18px; font-weight: 700; line-height: 22px; }
  .main-points p + p { margin-top: 22px; }

  .learn-more {
    position: absolute; right: 31px; top: 910px; width: 240px; text-align: right;
    color: var(--teal); font-size: 17px; line-height: 22px;
  }
  .links {
    position: absolute; right: 31px; top: 1042px; text-align: right;
    color: var(--red); font-size: 17.5px; line-height: 23px; font-weight: 700;
  }

  .partners { position: absolute; top: 1130px; left: 330px; width: 488px; height: 50px; }
  .partner {
    position: absolute; top: 0; height: 50px;
    display: flex; align-items: center; gap: 8px;
    font-size: 13px; line-height: 15px; font-weight: 700; color: var(--teal);
  }
  .partner-mark { width: 44px; height: 44px; border-radius: 50%; background: var(--teal); flex: none; }
  .partner-mark.square { border-radius: 0; width: 34px; height: 34px; background: var(--red); }
  .partner-one { left: 0; width: 220px; }
  .partner-two { left: 240px; width: 250px; }
</style>
</head>
<body>
<main class="flyer">
  <svg class="backdrop" width="848" height="1200" aria-hidden="true">
    <path d="M0 330 Q 150 470 150 650 Q 150 860 0 892 Z" fill="#e7e7e7"/>
    <path d="M848 0 L848 190 Q 760 120 700 0 Z" fill="#ececec"/>
  </svg>

  <h1 class="title"><strong>10 SIGNS</strong> OF <strong>THINKING</strong> OR <strong>MEMORY</strong><br><strong>CHANGES</strong> THAT MIGHT BE <strong>DEMENTIA</strong></h1>

  <section class="intro-band">
    <p>As we get older, we may slow down a bit. This is a normal part of aging. Changes in memory or thinking that make it harder to get through the day, are not a normal part of aging. These may be early signs of dementia.</p>
    <p>Because American Indian and Alaska Native people have a high risk of dementia, it is important to know the warning signs. Do you have any of these 10 signs? If so, talk to your doctor.</p>
  </section>

  <ol class="signs">
    <li class="sign" style="top:308px">
      <p class="sign-head"><b>1. MEMORY LOSS THAT AFFECTS YOUR DAILY LIFE.</b> You may:</p>
      <ul class="sign-points">
        <li>Forget events or important dates</li>
        <li>Repeat yourself</li>
        <li>Rely more often on lists or sticky notes to remember things</li>
      </ul>
    </li>
    <li class="sign" style="top:395px">
      <p class="sign-head"><b>2. TROUBLE PLANNING OR SOLVING PROBLEMS.</b> You may have a harder time:</p>
      <ul class="sign-points">
        <li>Paying bills</li>
        <li>Cooking recipes you have used for years</li>
      </ul>
    </li>
    <li class="sign" style="top:481px">
      <p class="sign-head"><b>3. GET CONFUSED ABOUT THE TIME, DATE, OR<br>WHERE YOU ARE.</b></p>
    </li>
    <li class="sign" style="top:529px">
      <p class="sign-head"><b>4. DAILY TASKS ARE GETTING HARDER,</b> including:</p>
      <ul class="sign-points">
        <li>Driving</li>
        <li>Making a grocery list or going shopping</li>
      </ul>
    </li>
    <li class="sign" style="top:595px">
      <p class="sign-head"><b>5. TROUBLE WITH HOW YOUR EYESIGHT AND<br>THINKING WORK TOGETHER THAT GETS WORSE.</b></p>
      <p class="sign-note">This includes:</p>
      <ul class="sign-points">
        <li>Tripping, falls, or problems with your balance</li>
        <li>Spilling or dropping things more</li>
      </ul>
    </li>
    <li class="sign" style="top:704px">
      <p class="sign-head"><b>6. NEW TROUBLE TALKING OR WRITING.</b> You have a hard time finding the words you want to say. For example, you may say “that thing on your wrist that tells time” instead of “watch.”</p>
    </li>
    <li class="sign" style="top:769px">
      <p class="sign-head"><b>7. LOSE AND CANNOT FIND THINGS.</b> For example, you:</p>
      <ul class="sign-points">
        <li>Can’t find the coffee pot that you use every day</li>
        <li>Might put your car keys in the freezer</li>
      </ul>
    </li>
    <li class="sign" style="top:838px">
      <p class="sign-head"><b>8. NOTICE CHANGES IN MOOD OR PERSONALITY,</b></p>
      <p class="sign-note">such as being:</p>
      <ul class="sign-points">
        <li>Easily mad or sad in everyday situations</li>
        <li>More fearful (scared) or suspicious (not trusting)</li>
      </ul>
    </li>
    <li class="sign" style="top:919px">
      <p class="sign-head"><b>9. ACT DIFFERENT AND MAKE POOR CHOICES.</b></p>
      <p class="sign-note">This may make you more likely to:</p>
      <ul class="sign-points">
        <li>Spend money you do not have or be a scam victim</li>
        <li>Stop washing up regularly or pay less attention to<br>how you look</li>
        <li>Forget to take care of your pet</li>
      </ul>
    </li>
    <li class="sign sign-ten" style="top:1042px">
      <p class="sign-head"><b>10. PULL AWAY FROM FRIENDS AND FAMILY<br>BECAUSE IT IS HARDER TO KEEP UP.</b> You may not want to do things you used to enjoy, like sporting events, church, music, or sex.</p>
    </li>
  </ol>

  <aside class="main-points">
    <h2>Main Points</h2>
    <p>American Indian and Alaska Native people have a high risk of dementia.</p>
    <p>Big changes in memory or thinking that make it hard to get through the day are not a normal part of aging.</p>
    <p>People with one or more of these 10 signs should talk to their doctor to find the cause. It is not always dementia.</p>
    <p>Early dementia diagnosis gives you a chance to get care and plan your future.</p>
  </aside>

  <p class="learn-more">To learn more about the warning signs of dementia in American Indian and Alaska Native people, visit:</p>
  <p class="links">www.NativeElderMind.org<br>www.agingwell-info.gov</p>

  <footer class="partners">
    <div class="partner partner-one"><span class="partner-mark"></span><span>Native Elders Brain Center</span></div>
    <div class="partner partner-two"><span class="partner-mark square"></span><span>Council for Native Aging</span></div>
  </footer>
</main>
</body>
</html>
```